DJ company new brochure of services offered

I would like to get a new price sheet made for my company services. Currently it's text only. I would like to add pictures next to each service description also like to add general background colors, and just make it look more attractive overall.

Uplighting - File #4 & file #10
Centerpiece pin-spots - File #15
Wedding Cake Spot - file #13 (can you crop out the logo at the bottom)?
Dance Floor Decal File #5
Gobo Monogram - File # 3
market lighting - file #14
ballroom draping - file #7
Video/projections screens: File #13
Indoor safe sparkler effect (not listed on price sheet yet) File #11
Dancing on a cloud - File #9
Co2 Cannons - File #6

Target Market(s)

bride and grooms

Industry/Entity Type

Entertainment

Font styles to use
Serif

Colors

Designer to choose colors to be used in the design.

Requirements
Must have
• my website is www.brightloomevents.example
• instagram is: @brightloomevents.example

```html
<!DOCTYPE html>
<html lang="en">
<head>
<meta charset="utf-8">
<title>Brightloom Events – Wedding Reception Price Sheet</title>
<link rel="stylesheet" href="https://fonts.googleapis.com/css2?family=Libre+Baskerville:wght@400;700&display=swap">
<style>
  :root {
    --band: #46474a;
    --ink: #3a3a3a;
    --white: #ffffff;
    --price-red: #e0201e;
    --box-line: #3f4043;
    --hero-a: #0c1420;
    --hero-b: #3b4a5c;
    --uplight-a: #4a3f38;
    --uplight-b: #7a6656;
    --drape-a: #c7a9cf;
    --drape-b: #8c6f9a;
    --floor-a: #5b4538;
    --floor-b: #8d725e;
    --spark-a: #3c3a3c;
    --spark-b: #8a8784;
  }
  * { box-sizing: border-box; margin: 0; padding: 0; }
  html, body { width: 848px; height: 1200px; overflow: hidden; background: var(--white); }
  body { font-family: "Libre Baskerville", Georgia, serif; color: var(--ink); }
  .sheet { position: relative; width: 848px; height: 1200px; }
  .abs { position: absolute; }

  .hero { left: 0; top: 0; width: 848px; height: 227px;
    background: radial-gradient(ellipse at 52% 40%, var(--hero-b), var(--hero-a) 75%); }
  .brand { left: 26px; top: 72px; color: var(--white); font-size: 20px; display: flex; align-items: center; gap: 8px; }
  .brand-dot { width: 12px; height: 12px; border-radius: 50%; background: var(--price-red); }
  .contact { right: 28px; top: 36px; text-align: right; color: var(--white); font-size: 12.5px; line-height: 17px; }
  .offerings { left: 0; width: 848px; top: 167px; text-align: center; color: var(--white); font-weight: 700; font-size: 18.5px; letter-spacing: 0.3px; }

  .band { left: 0; width: 848px; height: 43px; background: var(--band); color: var(--white);
    font-size: 17.5px; display: flex; align-items: center; justify-content: center; }

  .includes { left: 60px; width: 476px; text-align: center; font-size: 14.3px; line-height: 20.8px; }
  .includes b { font-weight: 700; }

  .price-card { left: 594px; width: 228px; border: 1.5px solid var(--box-line); }
  .price-card .day { background: var(--band); color: var(--white); height: 28px; display: flex; align-items: center; justify-content: center; font-size: 15px; position: relative; }
  .price-card .day::before { content: ""; position: absolute; left: 6px; top: 0; width: 2px; height: 18px; background: var(--white); }
  .price-card .amount { height: 72px; display: flex; align-items: center; justify-content: center; color: var(--price-red); font-size: 16px; font-weight: 700; }

  .photo { position: absolute; }
  .photo-uplight { left: 24px; top: 672px; width: 398px; height: 266px; background: linear-gradient(160deg, var(--uplight-b), var(--uplight-a)); }
  .photo-drape { left: 422px; top: 672px; width: 398px; height: 266px; background: linear-gradient(170deg, var(--drape-a), var(--drape-b)); }
  .photo-floor { left: 24px; top: 938px; width: 532px; height: 230px; background: linear-gradient(165deg, var(--floor-b), var(--floor-a)); }
  .photo-sparkler { left: 556px; top: 938px; width: 264px; height: 230px; background: linear-gradient(180deg, var(--spark-a), var(--spark-b)); }

  .overlay { position: absolute; color: var(--white); text-align: center; text-shadow: 0 1px 2px rgba(0,0,0,.45); }
  .overlay .title { font-weight: 700; font-size: 17px; line-height: 21px; }
  .overlay .detail { font-size: 14.2px; line-height: 20.5px; }
  .col-head { font-size: 17px; }
  .charge { position: absolute; color: var(--white); font-size: 14.5px; line-height: 20.5px; text-shadow: 0 1px 2px rgba(0,0,0,.45); }
  .footer-note { left: 24px; width: 796px; top: 1141px; font-size: 14px; }
</style>
</head>
<body>
<div class="sheet">

  <header>
    <div class="abs hero" role="img" aria-label="Couple's first dance on a misty ballroom floor with guests around"></div>
    <div class="abs brand"><span class="brand-dot"></span>Brightloom Events</div>
    <div class="abs contact">
      <div># 555.014.2290</div>
      <div>brightloomevents.example</div>
      <div>hello@brightloomevents.example</div>
      <div>Instagram- @brightloomevents.example</div>
    </div>
    <div class="abs offerings">DJ &nbsp;|&nbsp; LIGHTING &nbsp;|&nbsp; PRO AUDIO &nbsp;|&nbsp; VISUAL</div>
  </header>

  <section class="package">
    <div class="abs band" style="top:227px">5 Hour DJ/MC Wedding Reception Package</div>

    <div class="abs includes" style="top:288px">
      <b>This package includes:</b><br>
      Formally attired &amp; live mixing DJ<br>
      Emcee hosting all announcements<br>
      Powered speaker sound system<br>
      Wireless microphones for toasts speeches<br>
      In-person consultation to discuss event details<br>
      Online access to planning forms &amp; music database<br>
      Up to 6 hours of continuous entertainment
    </div>
    <div class="abs includes" style="top:496px">
      Ceremony music (<b>included</b>)<br>
      (includes sound equipment, wireless mic &amp; ceremony music)
    </div>
    <div class="abs includes" style="top:558px">
      Cocktail hour music (<b>included</b>)<br>
      (includes music in cocktail hour area)
    </div>

    <div class="abs price-card" style="top:296px"><div class="day">Monday-Thursday</div><div class="amount">$1295</div></div>
    <div class="abs price-card" style="top:406px"><div class="day">Friday &amp; Sunday</div><div class="amount">$1395</div></div>
    <div class="abs price-card" style="top:516px"><div class="day">Saturday</div><div class="amount">$1495</div></div>
  </section>

  <section class="extras">
    <div class="abs band" style="top:630px">Additional services (when booked with DJ package)</div>

    <div class="photo photo-uplight" role="img" aria-label="Ballroom with warm uplighting around round tables"></div>
    <div class="photo photo-drape" role="img" aria-label="Reception hall with lavender draping and crystal chandeliers"></div>
    <div class="photo photo-floor" role="img" aria-label="Reception room with white dance floor under market string lights"></div>
    <div class="photo photo-sparkler" role="img" aria-label="Couple dancing between indoor sparkler fountains"></div>

    <div class="overlay col-head" style="left:132px;width:200px;top:713px">Services</div>
    <div class="overlay col-head" style="left:534px;width:200px;top:716px">Charges</div>

    <div class="overlay" style="left:40px;width:420px;top:764px">
      <div class="title">Room uplighting (colour of your choice)</div>
      <div class="detail">20 fixtures (med-large room)<br>16 fixtures (med-large room)<br>12 fixtures (med-large room)</div>
    </div>
    <div class="charge" style="left:615px;top:786px">$400<br>$350<br>$300</div>

    <div class="overlay" style="left:40px;width:420px;top:870px">
      <div class="title">Pin-spot lighting</div>
      <div class="detail">(wedding cake/centerpieces/<br>sweetheart table etc.)</div>
    </div>
    <div class="charge" style="left:615px;top:872px">$30+</div>

    <div class="overlay" style="left:30px;width:440px;top:955px">
      <div class="title">Dance Floor decal/ Gobo Monogram</div>
      <div class="detail">(bride &amp; groom's names appear on the<br>wall or dance floor)</div>
    </div>
    <div class="charge" style="left:611px;top:958px">$250+</div>

    <div class="overlay" style="left:30px;width:440px;top:1041px">
      <div class="title">Seamless white dance floor with decal</div>
      <div class="detail">(square or round)</div>
    </div>
    <div class="charge" style="left:604px;top:1044px">$1000 +</div>

    <div class="overlay" style="left:30px;width:440px;top:1106px">
      <div class="title">Indoor safe sparkler effect</div>
    </div>

    <div class="overlay footer-note">We offer a wide range of additional services. Please contact us for more info &amp; pricing.</div>
  </section>

</div>
</body>
</html>
```